Business Card Design Project

Keep it simple , using logo and colors that compliment. Logo on one side with complimentary back ground color. Other side, personal info with possible complimentary design/colors

Target Market(s)

we are a non for profit that will be seeking donations . Both monetary and in kind

Industry/Entity Type

Business

Font styles to use
Sans Serif

Colors

Designer to choose colors to be used in the design.

```html
<!DOCTYPE html>
<html lang="en">
<head>
<meta charset="utf-8">
<title>Vellora Aid – Business Card</title>
<link rel="stylesheet" href="https://fonts.googleapis.com/css2?family=Questrial&display=swap">
<style>
  :root {
    --navy: #121a4a;
    --yellow: #f2ec12;
    --paper: #ffffff;
    --backdrop: #e9e7e3;
    --ink: #1d2350;
  }
  html, body {
    margin: 0;
    width: 1200px;
    height: 1000px;
    overflow: hidden;
    background: var(--backdrop);
    font-family: "Questrial", Arial, sans-serif;
  }
  .canvas {
    position: relative;
    width: 1200px;
    height: 1000px;
  }
  .card {
    position: absolute;
    left: 250px;
    width: 700px;
    height: 400px;
    box-shadow: 0 6px 18px rgba(0,0,0,0.18);
  }
  .card svg { display: block; width: 700px; height: 400px; overflow: hidden; }
  .card--info { top: 60px; background: var(--paper); }
  .card--brand { top: 540px; background: var(--navy); }
  .info-name { font-size: 27px; fill: var(--ink); }
  .info-title { font-size: 16px; fill: var(--ink); }
  .info-line { font-size: 16px; fill: var(--ink); }
  .icon { fill: var(--ink); }
  .brand-name { fill: var(--yellow); font-family: "Questrial", Arial, sans-serif; }
</style>
</head>
<body>
<main class="canvas">

  <!-- Personal info side -->
  <section class="card card--info" aria-label="Business card, contact side">
    <svg viewBox="0 0 700 400" xmlns="http://www.w3.org/2000/svg">
      <circle class="deco-arc-top" cx="420" cy="-175" r="220" fill="none" stroke="var(--navy)" stroke-width="3"/>
      <circle class="deco-disc-bottom" cx="440" cy="575" r="195" fill="var(--navy)" stroke="var(--yellow)" stroke-width="6"/>

      <text class="info-name" x="70" y="92">Your Name here</text>
      <text class="info-title" x="70" y="120">Title here</text>

      <!-- pin -->
      <path class="icon" d="M72 176a8 8 0 0 1 16 0c0 7-8 15-8 15s-8-8-8-15z M80 172a3.5 3.5 0 1 0 0.01 0z" fill-rule="evenodd"/>
      <text class="info-line" x="100" y="188">Address: To be confirmed</text>
      <!-- phone -->
      <rect class="icon" x="74" y="204" width="12" height="20" rx="2"/>
      <rect x="76.5" y="207" width="7" height="12" fill="var(--paper)"/>
      <text class="info-line" x="100" y="220">Phone: To be confirmed</text>
      <!-- fax -->
      <rect class="icon" x="71" y="242" width="18" height="12" rx="1.5"/>
      <rect class="icon" x="75" y="236" width="10" height="5"/>
      <text class="info-line" x="100" y="252">Fax: To be confirmed</text>
      <!-- email -->
      <rect class="icon" x="71" y="271" width="18" height="13" rx="1.5"/>
      <path d="M72 272l8 6 8-6" fill="none" stroke="var(--paper)" stroke-width="1.5"/>
      <text class="info-line" x="100" y="284">Email: hello@vellora-aid.example</text>

      <circle class="brand-disc" cx="610" cy="225" r="55" fill="var(--navy)" stroke="var(--yellow)" stroke-width="4"/>
      <text class="brand-name" x="610" y="231" font-size="16" text-anchor="middle">Vellora Aid</text>
    </svg>
  </section>

  <!-- Brand side -->
  <section class="card card--brand" aria-label="Business card, brand side">
    <svg viewBox="0 0 700 400" xmlns="http://www.w3.org/2000/svg">
      <circle class="deco-ring-large" cx="70" cy="50" r="205" fill="none" stroke="var(--yellow)" stroke-width="5"/>
      <circle class="deco-ring-thin" cx="60" cy="440" r="145" fill="none" stroke="var(--yellow)" stroke-width="2"/>
      <circle class="deco-ring-bold" cx="800" cy="410" r="200" fill="none" stroke="var(--yellow)" stroke-width="14"/>

      <circle class="brand-ring" cx="360" cy="200" r="92" fill="none" stroke="var(--yellow)" stroke-width="5"/>
      <text class="brand-name" x="360" y="211" font-size="28" text-anchor="middle">Vellora Aid</text>
    </svg>
  </section>

</main>
</body>
</html>
```